R&D and Engineering Management Consultancy Needs Branding

I need a branding style for my consultancy - specifically I need business cards by Tuesday 26 April (9 days away!) to take to a conference, including a logo design. If this service does not include printing I will need it in time for printing.

Later, the same logo and style needs to be incorporated into a Powerpoint template and a Word Template. Optionally also a Pages template.

The branding image needs to project and/or support the following qualities:
High tech
Speed and throughput
Lean
Innovation
Dependability
Quality

One possible concept is based on the Principal’s surname – Marrowby, which is a small bird. So a logo design which is a stylized rendition of a bird may work well. Flight implies speed, and the style would be “techy”, perhaps geometric in a way that conveys Lean – boiling things down to the essential elements.

Other concepts are welcome.
You can find me on https://au.peoplenexa.com/in/hollismarrowby

Business Card Information
Marrowby Consulting
Hollis Marrowby
BE (Hons), CSM, CSPO, SA
Principal Consultant
Mobile: +61 (0)455 913 607
Email: hollis@marrowbyconsulting.com
Web: www.marrowbyconsulting.com

Reverse:
Lean/Agile Software Development at Scale
Lean Product Development
Lean Portfolio Management
Organisational development and transformation
Mentoring and coaching of Technical Leaders
Program and project management
Business Processes and Systems

Target Market(s)

The target market for this consultancy comprises technology-based product and/or services development companies. They typically engage in one or a mix of software, electronics, mechanical, ASIC and MEMS development activities. They range from small startups to transnational corporations staffed by highly skilled engineers, developers and scientists. The consultancy is applicable across a range of domains such as biomedical device development, inkjet printing technology, telecommunications, internet and mesh networking technologies, renewable energy systems, and electronic product development of all kinds.

Industry/Entity Type

Information Technology

Contact Information for Business Card

Marrowby Consulting
Hollis Marrowby
BE (Hons), CSM, CSPO, SA
Principal Consulting

Reverse:
➢ Lean/Agile Software Development
➢ Lean Product Development
➢ Lean Portfolio Management
➢ Organisational development and transformation
➢ Mentoring and coaching of Technical Leaders
➢ Program and project management
➢ Business Processes and Systems

Logo Text

Just graphical

Font styles to use
Sans Serif

Requirements
Must have
• A clean professional look
Nice to have
• Use a bird motif based on my name Marrowby
• The bird's colours are yellow/gold, light brown, black and red so these suggest a colour scheme.
• I have uploaded a stylised bird design that I like but this belongs to another company. A variation on this might be good.
Should not have
• Too much clutter. If the details are too much to fit, drop the qualifications line

```html
<!DOCTYPE html>
<html lang="en">
<head>
<meta charset="utf-8">
<title>Marrowby Consulting – Business Cards</title>
<link rel="stylesheet" href="https://fonts.googleapis.com/css2?family=Lato:wght@400;700&display=swap">
<style>
  :root {
    --gold: #c8920a;
    --ink: #111111;
    --paper: #ffffff;
    --rule: #9a9a9a;
    --backdrop: #ecebe8;
  }
  * { margin: 0; padding: 0; box-sizing: border-box; }
  html, body { width: 1200px; height: 900px; overflow: hidden; }
  body {
    position: relative;
    background: var(--backdrop);
    font-family: "Lato", Arial, sans-serif;
  }
  .card {
    position: absolute;
    overflow: hidden;
    box-shadow: 0 6px 18px rgba(0,0,0,.18);
  }
  .card--front { left: 78px; top: 34px; width: 588px; height: 363px; background: var(--paper); }
  .card--back  { left: 388px; top: 505px; width: 566px; height: 352px; background: var(--gold); }

  .card__bands { position: absolute; inset: 0; }

  .wordmark {
    position: absolute;
    left: 0; right: 0;
    display: flex; align-items: center; justify-content: center; gap: 14px;
    font-weight: 700;
    font-size: 38px;
    letter-spacing: .5px;
  }
  .wordmark__dot { width: 30px; height: 30px; border-radius: 50%; flex: none; }
  .card--front .wordmark { top: 125px; color: var(--gold); }
  .card--front .wordmark__dot { background: var(--gold); }
  .card--back .wordmark { top: 120px; color: var(--paper); }
  .card--back .wordmark__dot { background: var(--paper); }

  .holder {
    position: absolute; right: 333px; top: 255px;
    text-align: right; color: var(--paper);
  }
  .card--front .holder { right: calc(588px - 255px); }
  .holder__name { font-size: 23px; font-weight: 400; line-height: 30px; }
  .holder__line { font-size: 16.5px; line-height: 22px; }

  .contacts {
    position: absolute; left: 284px; top: 262px;
    list-style: none; color: var(--paper);
    font-size: 17px; line-height: 24.5px;
  }
  .contacts li { display: flex; align-items: center; gap: 10px; }
  .contacts svg { width: 11px; height: 11px; fill: var(--paper); flex: none; }

  .services {
    position: absolute; left: 48px; right: 48px; top: 228px;
    text-align: center; color: var(--paper);
    font-size: 12.6px; line-height: 21.5px;
  }
</style>
</head>
<body>

<section class="card card--front" aria-label="Business card front">
  <svg class="card__bands" viewBox="0 0 588 363" aria-hidden="true">
    <polygon fill="var(--ink)" points="0,198 402,198 376,226 0,226"/>
    <polygon fill="var(--gold)" points="416,192 588,192 588,363 0,363 0,230 384,230"/>
  </svg>
  <div class="wordmark"><span class="wordmark__dot"></span>Marrowby Consulting</div>

  <div class="holder">
    <p class="holder__name">Hollis Marrowby</p>
    <p class="holder__line">BE (Hons), CSM, CSPO, SA</p>
    <p class="holder__line">Principal Consulting</p>
  </div>

  <ul class="contacts">
    <li><svg viewBox="0 0 12 12"><path d="M1 4c0-2 2-3 5-3s5 1 5 3l-2 1-1-2H4L3 5zM3 6h6l2 5H1z"/></svg>+61 (0)455 913 607</li>
    <li><svg viewBox="0 0 12 12"><path d="M0 2h12v1L6 7 0 3zM0 4.5l6 4 6-4V10H0z"/></svg>hollis@marrowbyconsulting.com</li>
    <li><svg viewBox="0 0 12 12"><path d="M5 7l2-2M3.5 6 1.8 7.7a1.8 1.8 0 0 0 2.5 2.5L6 8.5M8.5 6l1.7-1.7a1.8 1.8 0 0 0-2.5-2.5L6 3.5" stroke="var(--paper)" stroke-width="1.4" fill="none"/></svg>www.marrowbyconsulting.com</li>
  </ul>
</section>

<section class="card card--back" aria-label="Business card back">
  <div class="wordmark"><span class="wordmark__dot"></span>Marrowby Consulting</div>
  <p class="services">Lean/Agile Software Development - Lean Product Development - Lean Portfolio Management - Organisational development and transformation - Mentoring and coaching of Technical Leaders - Program and project management - Business Processes and Systems</p>
</section>

</body>
</html>
```